Medical marijuana business needs logo cleaned up and a packaging design.

We need a logo and packaging design for a new medical marijuana business in California called "Velvet Orchard". We produce high end medical grade e...
Target Market(s)
medical marijuana users
Industry/Entity Type
Business
Requirements
Nice to have
- Matte white background. Foil images and fonts

```html
<!DOCTYPE html>
<html lang="en">
<head>
<meta charset="utf-8">
<title>Velvet Orchard — Cartridge Package</title>
<link href="https://fonts.googleapis.com/css2?family=Cinzel:wght@700&family=Arimo:wght@400&display=swap" rel="stylesheet">
<style>
  :root {
    --paper: #ffffff;
    --leaf-green: #0a6a38;
    --ink-black: #0d0d0d;
    --foil-gold: #a06e2c;
    --foil-light: #f2cf6a;
    --foil-mid: #c9952f;
    --foil-deep: #7a5512;
    --label-white: #ffffff;
  }
  html, body {
    margin: 0;
    padding: 0;
    width: 1000px;
    height: 1200px;
    overflow: hidden;
    background: var(--paper);
  }
  .canvas {
    position: relative;
    width: 1000px;
    height: 1200px;
    background: var(--paper);
  }
  .package {
    position: absolute;
    left: 240px;
    top: 80px;
    width: 538px;
    height: 1073px;
    border-radius: 40px;
    overflow: hidden;
    background: linear-gradient(to bottom, var(--leaf-green) 0 598px, var(--ink-black) 598px 100%);
    box-shadow: 0 0 0 1px #000;
  }
  .package__frame {
    position: absolute;
    left: 22px;
    top: 20px;
    width: 494px;
    height: 1030px;
    box-sizing: border-box;
    border: 4px solid var(--foil-gold);
    border-radius: 34px;
    overflow: hidden;
    background: linear-gradient(to bottom, var(--paper) 0 578px, var(--ink-black) 578px 100%);
  }
  .category-title {
    position: absolute;
    left: 0;
    right: 0;
    top: 34px;
    margin: 0;
    text-align: center;
    font-family: "Cinzel", serif;
    font-weight: 700;
    font-size: 58px;
    letter-spacing: 1px;
    color: var(--leaf-green);
    line-height: 1;
  }
  .cartridge-photo {
    position: absolute;
    left: 193px;
    top: 145px;
    width: 100px;
    height: 433px;
    border-radius: 6px 6px 0 0;
    background: linear-gradient(to bottom, var(--foil-light) 0%, var(--foil-mid) 18%, var(--foil-deep) 40%, #8a7410 60%, #b59a22 100%);
  }
  .feature-list {
    position: absolute;
    top: 0;
    width: 180px;
    margin: 0;
    padding: 0;
    list-style: none;
    font-family: "Arimo", Arial, sans-serif;
    font-size: 20px;
    line-height: 28px;
    color: var(--leaf-green);
    text-align: center;
  }
  .feature-list li { position: absolute; left: 0; width: 180px; }
  .feature-list--left { left: 11px; }
  .feature-list--right { left: 300px; }
  .brand-name {
    position: absolute;
    left: 0;
    right: 0;
    margin: 0;
    text-align: center;
    font-family: "Cinzel", serif;
    font-weight: 700;
    font-size: 64px;
    color: var(--label-white);
    line-height: 1;
  }
  .brand-name--top { top: 598px; }
  .brand-name--bottom { top: 928px; }
  .brand-dot {
    position: absolute;
    left: 187px;
    top: 700px;
    width: 112px;
    height: 112px;
    border-radius: 50%;
    background: var(--foil-mid);
  }
</style>
</head>
<body>
<div class="canvas">
  <div class="package">
    <div class="package__frame">
      <h1 class="category-title">MARIJUANA</h1>

      <div class="cartridge-photo" role="img" aria-label="Product photo of a gold-capped glass vape cartridge filled with amber oil"></div>

      <ul class="feature-list feature-list--left">
        <li style="top:194px">Super<br>Premium<br>Concentrate</li>
        <li style="top:330px">Superior<br>Quartz<br>Cartidge</li>
        <li style="top:464px">Ultimate Flavor<br>Experience</li>
      </ul>
      <ul class="feature-list feature-list--right">
        <li style="top:184px">Lab Tested,<br>Contaminant<br>Free</li>
        <li style="top:306px">Most Potent<br>THC Cartridge<br>Available</li>
        <li style="top:442px">I gram of<br>Fire</li>
      </ul>

      <p class="brand-name brand-name--top">Velvet</p>
      <div class="brand-dot"></div>
      <p class="brand-name brand-name--bottom">Orchard</p>
    </div>
  </div>
</div>
</body>
</html>
```